Quorvane Strategic Solutions Nationwide Internet Marketing needs PowerPoint Template

We need a PowerPoint template for our sales division that goes through why we exist, products and capabilities and etc. First...we would like a background that is consent. The PowerPoint should be clean but with graphics that helps visually convey our offerings and culture. I've uploaded PowerPoints and a description of each slide we would like to carve out. You can also visit our website at www.quorvane.example

Target Market(s)

Nationwide.

Industry/Entity Type

Internet

Number of Pages Required

5+ page

Requirements
Must have
• Company Colors and Rhino
Nice to have
• Have a focus on a "WHY WE EXIST" touching on company core values/purpose
Should not have
• Company is 85% HVAC/Home services industry focused. We don't want sole focus on just the HVAC vertical. We are looking to expand into other verticals.

```html
<!DOCTYPE html>
<html lang="en">
<head>
<meta charset="utf-8">
<title>Quorvane Strategic Solutions – Slide Design Idea 01</title>
<link rel="stylesheet" href="https://fonts.googleapis.com/css2?family=Anton&family=Arimo:wght@400&family=Ubuntu:wght@500;700&family=Roboto+Condensed:wght@400&display=swap">
<style>
  :root {
    --sheet-bg: #000000;
    --heading-blue: #1b9ad0;
    --slide-top: #ffffff;
    --slide-bottom: #ececec;
    --brand-orange: #f5802a;
    --ink: #111111;
    --strip-dark: #2a2a2a;
    --step-one: #3d88c9;   --step-one-top: #2f6ea6;   --step-one-side: #285b88;
    --step-two: #e2a640;   --step-two-top: #c08a2c;   --step-two-side: #9b7128;
    --step-three: #ffcf00; --step-three-top: #d7ad00; --step-three-side: #b08d12;
    --step-four: #ff0000;  --step-four-top: #d60b0b;  --step-four-side: #a41212;
    --step-five: #5a4fc8;  --step-five-top: #4a40b2;  --step-five-side: #3d3596;
    --figure-grey: #5c5c5c;
    --silhouette: #2a2a2a;
  }
  * { margin: 0; padding: 0; box-sizing: border-box; }
  html, body { width: 1200px; height: 1200px; overflow: hidden; background: var(--sheet-bg); }
  .sheet { position: relative; width: 1200px; height: 1200px; }
  .sheet-title {
    position: absolute; top: 12px; left: 0; width: 1200px; text-align: center;
    font-family: "Roboto Condensed", sans-serif; font-weight: 400; font-size: 37px; color: var(--heading-blue);
    letter-spacing: 1px;
  }
  .sheet-note {
    position: absolute; top: 68px;
    font-family: "Roboto Condensed", sans-serif; font-size: 18px; color: var(--heading-blue);
  }
  .sheet-note--left { left: 163px; }
  .sheet-note--right { left: 596px; }
  .slide { position: absolute; width: 902px; height: 492px; }
  .slide--first { left: 138px; top: 114px; }
  .slide--second { left: 142px; top: 658px; }
  .slide svg { display: block; width: 100%; height: 100%; }
  .slide-title { font-family: "Anton", sans-serif; font-size: 56px; fill: var(--ink); letter-spacing: -1px; }
  .brand-name { font-family: "Ubuntu", sans-serif; font-weight: 700; fill: var(--ink); }
  .step-label { font-family: "Arimo", sans-serif; font-weight: 400; font-size: 24px; fill: #ffffff; text-anchor: middle; }
  .step-copy { font-family: "Ubuntu", sans-serif; font-weight: 500; font-size: 21px; fill: var(--ink); text-anchor: middle; }
</style>
</head>
<body>
<main class="sheet">
  <h1 class="sheet-title">SLIDE DESIGN IDEA - 01</h1>
  <p class="sheet-note sheet-note--left">HERE I’M SHOWING THE IMPORTANT SLIDES ONLY</p>
  <p class="sheet-note sheet-note--right">( ANY MODIFICATIONS SUGESTED WILL BE ADDRESSED)</p>

  <section class="slide slide--first">
    <svg viewBox="0 0 1128 615" xmlns="http://www.w3.org/2000/svg">
      <defs>
        <linearGradient id="slideFillA" x1="0" y1="0" x2="0" y2="1">
          <stop offset="0" stop-color="var(--slide-top)"/><stop offset="1" stop-color="var(--slide-bottom)"/>
        </linearGradient>
        <linearGradient id="landscapeA" x1="0" y1="0" x2="0" y2="1">
          <stop offset="0" stop-color="#f0f0f0"/><stop offset="1" stop-color="var(--silhouette)"/>
        </linearGradient>
      </defs>
      <rect class="slide-bg" width="1128" height="615" fill="url(#slideFillA)"/>
      <rect class="top-band" width="886" height="22" fill="var(--brand-orange)"/>
      <g class="brand-block">
        <text class="brand-name" x="1010" y="40" font-size="32" text-anchor="middle">QUORVANE</text>
        <text class="brand-name" x="1010" y="60" font-size="13" text-anchor="middle">STRATEGIC SOLUTIONS</text>
      </g>
      <text class="slide-title" x="121" y="113">5 STEPS TO ONLINE SUCCESS</text>

      <g class="step step--one">
        <polygon points="108,448 258,448 290,456 140,456" fill="var(--step-one-top)"/>
        <polygon points="108,448 140,456 140,488 108,468" fill="var(--step-one-side)"/>
        <rect x="140" y="456" width="150" height="32" fill="var(--step-one)"/>
        <text class="step-label" x="216" y="481">One</text>
      </g>
      <g class="step step--two">
        <polygon points="292,388 442,388 470,398 325,398" fill="var(--step-two-top)"/>
        <polygon points="292,388 325,398 325,436 292,416" fill="var(--step-two-side)"/>
        <rect x="325" y="398" width="145" height="38" fill="var(--step-two)"/>
        <text class="step-label" x="398" y="425">Two</text>
      </g>
      <g class="step step--three">
        <polygon points="471,336 623,336 655,345 503,345" fill="var(--step-three-top)"/>
        <polygon points="471,336 503,345 503,385 471,363" fill="var(--step-three-side)"/>
        <rect x="503" y="345" width="152" height="40" fill="var(--step-three)"/>
        <text class="step-label" x="580" y="373">Three</text>
      </g>
      <g class="step step--four">
        <polygon points="656,265 821,265 851,275 686,275" fill="var(--step-four-top)"/>
        <polygon points="656,265 686,275 686,318 656,294" fill="var(--step-four-side)"/>
        <rect x="686" y="275" width="165" height="43" fill="var(--step-four)"/>
        <text class="step-label" x="770" y="304">Four</text>
      </g>
      <g class="step step--five">
        <polygon points="862,224 1024,224 1055,233 893,233" fill="var(--step-five-top)"/>
        <polygon points="862,224 893,233 893,276 862,252" fill="var(--step-five-side)"/>
        <rect x="893" y="233" width="162" height="43" fill="var(--step-five)"/>
        <text class="step-label" x="975" y="262">Five</text>
      </g>

      <rect class="climber" x="433" y="218" width="80" height="148" rx="10" fill="var(--figure-grey)" opacity="0.35" role="img" aria-label="Walking figure climbing the steps"/>

      <text class="step-copy" x="220" y="520"><tspan x="220">Make Your</tspan><tspan x="220" dy="25">Website Convert</tspan><tspan x="220" dy="25">Quality Leads</tspan></text>
      <text class="step-copy" x="400" y="459"><tspan x="400">SEO</tspan><tspan x="400" dy="26">Rank High For As</tspan><tspan x="400" dy="25">Many Keywords</tspan><tspan x="400" dy="25">As Possible</tspan></text>
      <text class="step-copy" x="584" y="425"><tspan x="584">PPC</tspan><tspan x="584" dy="26">Focussed Keywords</tspan><tspan x="584" dy="25">That Convert To</tspan><tspan x="584" dy="25">Real Leads</tspan></text>

      <rect class="landscape" x="808" y="495" width="265" height="108" fill="url(#landscapeA)" role="img" aria-label="Savanna silhouette with a rhino beneath an acacia tree"/>
      <rect class="bottom-band" y="603" width="1128" height="7" fill="var(--brand-orange)"/>
      <rect class="bottom-strip" y="610" width="1128" height="5" fill="var(--strip-dark)"/>
    </svg>
  </section>

  <section class="slide slide--second">
    <svg viewBox="0 0 1126 621" xmlns="http://www.w3.org/2000/svg">
      <defs>
        <linearGradient id="slideFillB" x1="0" y1="0" x2="0" y2="1">
          <stop offset="0" stop-color="var(--slide-top)"/><stop offset="1" stop-color="var(--slide-bottom)"/>
        </linearGradient>
        <linearGradient id="landscapeB" x1="0" y1="0" x2="0" y2="1">
          <stop offset="0" stop-color="#f0f0f0"/><stop offset="1" stop-color="var(--silhouette)"/>
        </linearGradient>
      </defs>
      <rect class="slide-bg" width="1126" height="621" fill="url(#slideFillB)"/>
      <rect class="top-band" width="884" height="22" fill="var(--brand-orange)"/>
      <g class="brand-block">
        <text class="brand-name" x="1009" y="40" font-size="32" text-anchor="middle">QUORVANE</text>
        <text class="brand-name" x="1009" y="60" font-size="13" text-anchor="middle">STRATEGIC SOLUTIONS</text>
      </g>
      <text class="slide-title" x="121" y="114">5 STEPS TO ONLINE SUCCESS</text>

      <g class="step step--one">
        <polygon points="109,454 259,454 290,463 141,463" fill="var(--step-one-top)"/>
        <polygon points="109,454 141,463 141,492 109,474" fill="var(--step-one-side)"/>
        <rect x="141" y="463" width="149" height="29" fill="var(--step-one)"/>
        <text class="step-label" x="216" y="485">One</text>
      </g>
      <g class="step step--two">
        <polygon points="292,393 442,393 470,403 325,403" fill="var(--step-two-top)"/>
        <polygon points="292,393 325,403 325,440 292,421" fill="var(--step-two-side)"/>
        <rect x="325" y="403" width="145" height="37" fill="var(--step-two)"/>
        <text class="step-label" x="398" y="430">Two</text>
      </g>
      <g class="step step--three">
        <polygon points="471,340 621,340 653,349 503,349" fill="var(--step-three-top)"/>
        <polygon points="471,340 503,349 503,389 471,367" fill="var(--step-three-side)"/>
        <rect x="503" y="349" width="150" height="40" fill="var(--step-three)"/>
        <text class="step-label" x="578" y="377">Three</text>
      </g>
      <g class="step step--four">
        <polygon points="655,268 819,268 849,277 684,277" fill="var(--step-four-top)"/>
        <polygon points="655,268 684,277 684,321 655,297" fill="var(--step-four-side)"/>
        <rect x="684" y="277" width="165" height="44" fill="var(--step-four)"/>
        <text class="step-label" x="768" y="307">Four</text>
      </g>
      <g class="step step--five">
        <polygon points="860,227 1021,227 1052,235 891,235" fill="var(--step-five-top)"/>
        <polygon points="860,227 891,235 891,279 860,254" fill="var(--step-five-side)"/>
        <rect x="891" y="235" width="161" height="44" fill="var(--step-five)"/>
        <text class="step-label" x="972" y="265">Five</text>
      </g>

      <rect class="climber" x="622" y="147" width="78" height="148" rx="10" fill="var(--figure-grey)" opacity="0.35" role="img" aria-label="Walking figure climbing the steps"/>

      <text class="step-copy" x="221" y="525"><tspan x="221">Make Your</tspan><tspan x="221" dy="25">Website Convert</tspan><tspan x="221" dy="26">Quality Leads</tspan></text>
      <text class="step-copy" x="400" y="465"><tspan x="400">SEO</tspan><tspan x="400" dy="26">Rank High For As</tspan><tspan x="400" dy="25">Many Keywords</tspan><tspan x="400" dy="25">As Possible</tspan></text>
      <text class="step-copy" x="583" y="430"><tspan x="583">PPC</tspan><tspan x="583" dy="26">Focussed Keywords</tspan><tspan x="583" dy="25">That Convert To</tspan><tspan x="583" dy="26">Real Leads</tspan></text>
      <text class="step-copy" x="773" y="359"><tspan x="773">Track Every Lead,</tspan><tspan x="773" dy="25">Cost Per Lead</tspan><tspan x="773" dy="25">And Revenue</tspan></text>

      <rect class="landscape" x="808" y="500" width="265" height="108" fill="url(#landscapeB)" role="img" aria-label="Savanna silhouette with a rhino beneath an acacia tree"/>
      <rect class="bottom-band" y="608" width="1126" height="7" fill="var(--brand-orange)"/>
      <rect class="bottom-strip" y="615" width="1126" height="6" fill="var(--strip-dark)"/>
    </svg>
  </section>
</main>
</body>
</html>
```